New company website for Redfern Hollow Building Company

We're looking to build a new company website that customers can use to contact us, get quotes, view past projects (renovations, additions, new construction, etc.), & learn more about our business. We want to use WordPress for our website and have already purchased the Divi theme (by Quillmark Studio). Using that theme isn't required but we already have several examples of websites that we want to model our site after that use this theme. The "look" we're after is simple, light, & clean.

Target Market(s)

Residential remodeling, renovations, and new construction.

Industry/Entity Type

Residential Construction

Coding

Coded - Design and coding required

Number of Pages Required

5+ page

Font styles to use
Sans Serif

Colors
33a6d7
aaaaaa

Requirements
Must have
• We require the website to be coded using the Divi theme. We'll be upgrading the project to include this today or tomorrow.
• The navigation bar should be static & remain at the top of the page. When scrolling we'd like the logo & info in the nav bar to size down. Here's an example of a site that does this: https://tovamerihomes.example/
Nice to have
• In the gallery with pictures of our finished product/jobs, when you mouse over the image, we'd like there to be additional info that shows up. For example, look at this gallery: https://tovamerihomes.example/projectcategories/kitchens/ We'll add a name/location of the job like: "Garvey kitchen - Millbrook, N.C."
• If you go to this website: https://plinvorworks.example/ and scroll down to the pictures, we like how the picture moves and is interactive.

```html
<!DOCTYPE html>
<html lang="en">
<head>
<meta charset="utf-8">
<title>Redfern Hollow Building Company</title>
<link href="https://fonts.googleapis.com/css2?family=Poppins:wght@400;500;600;700;800&family=Open+Sans:wght@400;600&display=swap" rel="stylesheet">
<style>
:root{
  --blue:#33a6d7;
  --grey:#aaaaaa;
  --ink:#1d1f24;
  --dark:#15171b;
  --text:#6b6e74;
  --light:#ececec;
  --paper:#ffffff;
}
*{box-sizing:border-box;margin:0;padding:0}
html,body{width:1200px;height:4452px;overflow:hidden}
body{position:relative;background:var(--paper);font-family:"Open Sans",sans-serif;color:var(--text);font-size:14px;line-height:1.6}
.abs{position:absolute;left:0;width:1200px}
h1,h2,h3,h4,.btn,.nav a,.logo{font-family:"Poppins",sans-serif}
.btn{display:inline-block;background:var(--ink);color:#fff;font-size:11px;font-weight:600;letter-spacing:.5px;padding:11px 22px;text-transform:uppercase;white-space:nowrap;line-height:1.4}
.btn-blue{background:var(--blue)}
.dots{display:flex;justify-content:center;gap:5px}
.dots i{width:6px;height:6px;border-radius:50%;background:var(--blue)}
.dots i:nth-child(2){background:var(--grey)}
.kicker{text-align:center;font-size:12px;color:var(--ink);margin-top:8px}
.sec-title{text-align:center;font-size:32px;font-weight:700;color:var(--ink);text-transform:uppercase;line-height:1.2;margin-top:4px}
.sec-sub{text-align:center;font-size:13px;width:560px;margin:10px auto 0}

/* top bar */
.topbar{top:0;height:32px;background:var(--dark);display:flex;align-items:center;justify-content:space-between;padding:0 120px;color:#ccc;font-size:11px}
.social{display:flex;gap:10px}
.social i{width:9px;height:9px;background:#bbb;border-radius:50%}
.contact-mini{display:flex;gap:22px;align-items:center}
.contact-mini span{display:flex;gap:6px;align-items:center}

/* header */
.header{top:32px;height:88px;background:#fff;display:flex;align-items:center;justify-content:space-between;padding:0 120px;box-shadow:0 2px 6px rgba(0,0,0,.15);z-index:5}
.logo{color:#2a3644;font-weight:700;font-size:24px;line-height:1;text-transform:uppercase;letter-spacing:1px}
.logo small{display:block;font-size:12.5px;letter-spacing:3.3px;margin-top:4px}
.nav{display:flex}
.nav a{font-size:11px;font-weight:600;color:var(--ink);padding:0 12px;border-left:1px solid #ddd;text-decoration:none}
.nav a:first-child{border-left:0}

/* hero */
.hero{top:120px;height:480px;background:linear-gradient(100deg,#0f1318 0%,#1e2a36 45%,#2d3a46 70%,#161b21 100%)}
.hero-copy{position:absolute;left:130px;top:120px;color:#fff;width:460px}
.hero-copy h1{font-size:44px;font-weight:800;line-height:1}
.hero-copy h1 span{color:var(--blue)}
.hero-copy h4{font-size:16px;font-weight:500;margin-top:6px}
.hero-copy p{font-size:12px;color:#c9ced4;margin:10px 0 22px;width:340px}
.hero-dots{position:absolute;left:130px;top:404px;display:flex;gap:6px}
.hero-dots i{width:8px;height:8px;border-radius:50%;background:#fff;opacity:.5}
.hero-dots i:first-child{opacity:1}
.quote{position:absolute;left:780px;top:220px;width:320px;height:420px;background:var(--blue);padding:26px 40px;z-index:4}
.quote h3{color:#fff;font-size:16px;font-weight:600;text-align:center;text-transform:uppercase;margin-bottom:14px}
.field{background:#fff;height:30px;margin-bottom:12px;font-size:11px;color:#999;padding:6px 10px;display:flex;justify-content:space-between}
.field.area{height:80px}
.quote .btn{margin:6px auto 0;display:table}

/* why */
.why{top:600px;height:440px}
.why .dots{margin-top:70px}
.features{position:absolute;left:60px;top:220px;width:1080px;height:180px;display:grid;grid-template-columns:repeat(3,1fr)}
.feature{background:#efefef;padding:40px 30px;display:flex;gap:16px}
.feature.active{background:var(--blue);color:#fff}
.feature .ico{flex:none;width:42px;height:42px;border-radius:50%;background:var(--blue);display:flex;align-items:center;justify-content:center}
.feature.active .ico{background:#fff}
.feature h4{font-size:14px;font-weight:600;color:var(--ink);text-transform:uppercase}
.feature.active h4{color:#fff}
.feature p{font-size:11.5px;line-height:1.5}
.feature:not(.active) p{color:var(--text)}

/* about */
.about{top:1060px;height:520px;background:#e9e9e9}
.about-copy{position:absolute;left:110px;top:110px;width:480px}
.about-copy h2{font-size:38px;font-weight:700;color:var(--ink);line-height:1.1;text-transform:uppercase}
.about-copy h2 span{color:var(--blue)}
.about-copy p{font-size:12.5px;margin:22px 0 26px}
.about-media{position:absolute;left:720px;top:-20px;width:480px;height:540px;background:linear-gradient(160deg,#3a6fb5 0%,#7fa6d6 40%,#8a8a88 75%,#4d4a46 100%)}
.play{position:absolute;left:212px;top:242px;width:56px;height:56px;background:var(--blue);display:flex;align-items:center;justify-content:center}

/* specialties */
.specialties{top:1620px;height:680px}
.special-grid{position:absolute;left:80px;top:200px;width:1040px;display:grid;grid-template-columns:repeat(3,300px);gap:70px}
.special .img{height:220px;position:relative}
.special .badge{position:absolute;left:122px;bottom:-28px;width:56px;height:56px;border-radius:50%;border:4px solid #fff}
.special h3{margin-top:44px;text-align:center;color:var(--blue);font-size:16px;font-weight:600;text-transform:uppercase}
.special p{text-align:center;font-size:12px;margin-top:6px}
.specialties .btn{position:absolute;left:530px;top:610px}

/* projects */
.projects{top:2320px;height:860px;background:linear-gradient(180deg,#1a1d21 0%,#2b2e31 55%,#1a1c1f 100%)}
.projects .dots{margin-top:50px}
.projects .kicker,.projects .sec-title{color:#fff}
.projects .sec-sub{color:#b7bcc2}
.tabs{position:absolute;left:320px;top:208px;width:560px;display:flex;justify-content:space-between;font-family:"Poppins",sans-serif;font-size:11px;color:#aaa;text-transform:uppercase;border-bottom:1px solid #555}
.tabs span{padding:6px 10px}
.tabs .on{color:#fff;border-bottom:2px solid var(--blue)}
.gallery{position:absolute;left:120px;top:280px;width:960px;height:440px;display:grid;grid-template-columns:300px 420px 240px;grid-template-rows:220px 220px}
.tile-a{grid-row:1/3;background:linear-gradient(180deg,#6d92b8,#4a6b8f 60%,#3b3a38)}
.tile-b{background:linear-gradient(180deg,#90b2d4,#6f8fae 55%,#7c6f60)}
.tile-c{background:linear-gradient(180deg,#3f6fa8,#7f9fc1)}
.tile-d{background:var(--blue);display:flex;flex-direction:column;align-items:center;justify-content:center;color:#fff;font-family:"Poppins",sans-serif}
.tile-d small{font-size:11px}
.tile-d b{font-size:14px;font-weight:600}
.tile-e{background:linear-gradient(160deg,#b7c5cf,#6e7780 60%,#c5a23a)}
.projects .btn{position:absolute;left:546px;top:770px;background:#0c0d0f;border:1px solid #444}

/* team */
.team{top:3180px;height:900px;background:var(--light)}
.team .dots{margin-top:50px}
.team-grid{position:absolute;left:60px;top:170px;width:1080px;display:grid;grid-template-columns:repeat(4,255px);gap:20px}
.member .img{height:300px;background:linear-gradient(180deg,#5f8f3c,#3c6a2a 60%,#2b3a52)}
.member h4{margin-top:18px;text-align:center;color:var(--blue);font-size:13px;font-weight:600;text-transform:uppercase}
.member p{text-align:center;font-size:11.5px;margin-top:8px;padding:0 10px}
.member .btn{display:table;margin:20px auto 0}

/* newsletter */
.newsletter{top:4080px;height:60px;background:var(--blue);display:flex;align-items:center;justify-content:center;gap:60px}
.newsletter h4{color:#fff;font-size:15px;font-weight:600}
.sub-box{display:flex;width:440px;height:34px;background:#fff;border-radius:17px;align-items:center;justify-content:space-between;padding-left:16px;font-size:11px;color:#999}
.sub-box .btn{border-radius:17px;padding:10px 20px}

/* footer */
.footer{top:4140px;height:280px;display:grid;grid-template-columns:repeat(4,1fr);padding:40px 110px 0;gap:30px}
.footer h4{font-size:13px;font-weight:700;color:var(--ink);text-transform:uppercase;margin-bottom:14px}
.footer p,.footer li{font-size:11.5px;line-height:1.7}
.footer ul{list-style:none}
.footer li{display:flex;gap:8px;align-items:center;margin-bottom:6px}
.footer li::before{content:"";width:6px;height:6px;border-radius:50%;background:var(--blue)}
.contact-list li::before{display:none}
.contact-list b{color:var(--ink);width:54px;flex:none;font-weight:600}
.f-social{display:flex;gap:8px;margin-top:14px}
.f-social i{width:24px;height:24px;border-radius:50%;background:var(--ink)}
.thumbs{display:grid;grid-template-columns:repeat(3,62px);gap:6px}
.thumbs i{height:48px;background:linear-gradient(160deg,#7f9fc1,#5a5550)}
.copyright{top:4420px;height:32px;border-top:1px solid #ddd;display:flex;align-items:center;justify-content:center;font-size:10px;color:#888;letter-spacing:.5px}
</style>
</head>
<body>

<div class="abs topbar">
  <div class="social"><i></i><i></i><i></i></div>
  <div class="contact-mini">
    <span><svg width="12" height="9" viewBox="0 0 12 9"><rect x=".5" y=".5" width="11" height="8" fill="none" stroke="#33a6d7"/><path d="M.5 .5L6 5l5.5-4.5" fill="none" stroke="#33a6d7"/></svg>info@redfernhollow.example</span>
    <span><svg width="10" height="10" viewBox="0 0 10 10"><path d="M2 0l2 2.5-1.2 1.3a6 6 0 003.4 3.4L7.5 6 10 8l-1.5 2C4 10 0 6 0 1.5z" fill="#33a6d7"/></svg>+1 555 014 7590</span>
  </div>
</div>

<header class="abs header">
  <div class="logo">Redfern Hollow<small>Building Company</small></div>
  <nav class="nav"><a>GETTING STARTED</a><a>WHO WE ARE</a><a>SPECIALTIES</a><a>PORTFOLIO</a><a>CONTACT US</a></nav>
</header>

<section class="abs hero" role="img" aria-label="Dark photograph of a builder's hands over construction plans">
  <div class="hero-copy">
    <h1><span>BUILT ON</span> INTEGRITY</h1>
    <h4>We Do Big Things with Big Ideas</h4>
    <p>Lorem ipsum dolor sit amet, consectetur adipiscing elit, sed diam nonummy tempor incididunt ut labore.</p>
    <span class="btn btn-blue">Check Project</span>
  </div>
  <div class="hero-dots"><i></i><i></i><i></i></div>
</section>

<form class="quote">
  <h3>Request a Quote</h3>
  <div class="field">Name</div>
  <div class="field">Email Address</div>
  <div class="field">Project Type <span>▾</span></div>
  <div class="field">Your Budget <span>▾</span></div>
  <div class="field area">Project Details</div>
  <span class="btn">Submit</span>
</form>

<section class="abs why">
  <div class="dots"><i></i><i></i><i></i></div>
  <p class="kicker">Lorem ipsum dolor sit amet, consectetur</p>
  <h2 class="sec-title">Why Choose Us</h2>
  <p class="sec-sub">Lorem ipsum dolor sit amet, consectetur adipiscing elit, sed nam nec eros eget pellen</p>
  <div class="features">
    <div class="feature active">
      <div class="ico"><svg width="20" height="20" viewBox="0 0 20 20"><circle cx="10" cy="10" r="7" fill="none" stroke="#33a6d7" stroke-width="2"/><circle cx="10" cy="10" r="2.5" fill="#33a6d7"/></svg></div>
      <div><h4>Diversity</h4><p>Sed ut perspiciatis unde omnis iste natus error sit voluptatem accusantium doloremque</p></div>
    </div>
    <div class="feature">
      <div class="ico"><svg width="20" height="20" viewBox="0 0 20 20"><rect x="3" y="4" width="14" height="13" fill="none" stroke="#fff" stroke-width="2"/><path d="M3 8h14M7 2v4M13 2v4" stroke="#fff" stroke-width="2"/></svg></div>
      <div><h4>Early Planning</h4><p>Sed ut perspiciatis unde omnis iste natus error sit voluptatem accusantium doloremque</p></div>
    </div>
    <div class="feature">
      <div class="ico"><svg width="20" height="20" viewBox="0 0 20 20"><path d="M2 12l5 4 11-11" fill="none" stroke="#fff" stroke-width="2.4"/></svg></div>
      <div><h4>Client Service Provider</h4><p>Sed ut perspiciatis unde omnis iste natus error sit voluptatem accusantium doloremque</p></div>
    </div>
  </div>
</section>

<section class="abs about">
  <div class="about-copy">
    <h2>We Are<br>Best Construction<br><span>Company</span></h2>
    <p>Sed ut perspiciatis unde omnis iste natus error sit voluptatem accusantium doloremque laudantium, totam rem aperiam, eaque ipsa quae ab illo inventore veritatis et quasi architecto beatae vitae dicta sunt explicabo. Nemo enim ipsam voluptatem quia voluptas sit aspernatur aut odit aut fugit.</p>
    <span class="btn">Read More</span>
  </div>
  <div class="about-media" role="img" aria-label="Photograph of a high-rise under construction with tower cranes against a blue sky">
    <div class="play"><svg width="18" height="20" viewBox="0 0 18 20"><path d="M2 1l15 9-15 9z" fill="#fff"/></svg></div>
  </div>
</section>

<section class="abs specialties">
  <div class="dots"><i></i><i></i><i></i></div>
  <p class="kicker">Lorem ipsum dolor sit amet, consectetur</p>
  <h2 class="sec-title">Our Specialties</h2>
  <p class="sec-sub">Lorem ipsum dolor sit amet, consectetur adipiscing elit, sed nam nec eros eget pellen nisl sed feugiat nisi, morbi vehicula et bibendum lacinia</p>
  <div class="special-grid">
    <div class="special">
      <div class="img" role="img" aria-label="Photograph of a new home frame under construction" style="background:linear-gradient(160deg,#8aa4bd,#7a6a55 60%,#4a4038)"><span class="badge" style="background:#e8a32c"></span></div>
      <h3>New Home Construction</h3>
      <p>Sed ut perspiciatis unde omnis iste natus error sit voluptatem accusantium doloremque laudantium, totam rem aperiam, eaque</p>
    </div>
    <div class="special">
      <div class="img" role="img" aria-label="Photograph of a builder adding onto a house" style="background:linear-gradient(160deg,#c8d4dd,#d9a640 55%,#7b6a50)"><span class="badge" style="background:#5fb34d"></span></div>
      <h3>Additions</h3>
      <p>Sed ut perspiciatis unde omnis iste natus error sit voluptatem accusantium doloremque laudantium, totam rem aperiam, eaque</p>
    </div>
    <div class="special">
      <div class="img" role="img" aria-label="Photograph of a remodeling plan being reviewed" style="background:linear-gradient(160deg,#e2e5e8,#c6b8a6 55%,#8d7b6a)"><span class="badge" style="background:#d9443a"></span></div>
      <h3>Remodeling</h3>
      <p>Sed ut perspiciatis unde omnis iste natus error sit voluptatem accusantium doloremque laudantium, totam rem aperiam, eaque</p>
    </div>
  </div>
  <span class="btn">View All Services</span>
</section>

<section class="abs projects" role="img" aria-label="Dim photograph of a construction site at dusk behind the projects gallery">
  <div class="dots"><i></i><i></i><i></i></div>
  <p class="kicker">Lorem ipsum dolor sit amet</p>
  <h2 class="sec-title">Our Projects</h2>
  <p class="sec-sub">Lorem ipsum dolor sit amet, consectetur adipiscing elit, sed nam nec eros eget pellen nisl sed feugiat nisi, morbi vehicula et bibendum lacinia</p>
  <div class="tabs"><span class="on">On Going Project</span><span>Completed Project</span><span>Upcoming Project</span></div>
  <div class="gallery">
    <div class="tile-a" role="img" aria-label="Photograph of cranes over a building site"></div>
    <div class="tile-b" role="img" aria-label="Photograph of steel framing on a job site"></div>
    <div class="tile-c" role="img" aria-label="Photograph of a tower crane against the sky"></div>
    <div class="tile-d"><small>Garvey Kitchen</small><b>Millbrook, N.C.</b></div>
    <div class="tile-e" role="img" aria-label="Photograph of a worker in a hard hat on site"></div>
  </div>
  <span class="btn">Our Projects</span>
</section>

<section class="abs team">
  <div class="dots"><i></i><i></i><i></i></div>
  <p class="kicker">Lorem ipsum dolor sit amet</p>
  <h2 class="sec-title">Our Team</h2>
  <div class="team-grid">
    <div class="member">
      <div class="img" role="img" aria-label="Portrait photograph of team member"></div>
      <h4>Dorian Feltsworth</h4>
      <p>Dorian manages client and field projects, from scheduling to final touches on all new remodeling jobs, having grown up here</p>
      <span class="btn">Read More</span>
    </div>
    <div class="member">
      <div class="img" role="img" aria-label="Portrait photograph of team member"></div>
      <h4>Milo Harrandt</h4>
      <p>A lifelong local and state college graduate with a degree in Business and Finance, Milo has been a part of the crew</p>
      <span class="btn">Read More</span>
    </div>
    <div class="member">
      <div class="img" role="img" aria-label="Portrait photograph of team member"></div>
      <h4>Corwin Ashdale</h4>
      <p>Founder Corwin divides his time between directing sales and managing projects from a hands-on approach on every build</p>
      <span class="btn">Read More</span>
    </div>
    <div class="member">
      <div class="img" role="img" aria-label="Portrait photograph of team member"></div>
      <h4>Tobias Ashdale</h4>
      <p>President Tobias manages the daily work of the team with a passion for interior remodeling and small business growth</p>
      <span class="btn">Read More</span>
    </div>
  </div>
</section>

<section class="abs newsletter">
  <h4>Subscribe For Newsletter</h4>
  <div class="sub-box">Enter your email address<span class="btn">Subscribe</span></div>
</section>

<footer class="abs footer">
  <div>
    <h4>Information</h4>
    <p>Sed ut perspiciatis unde omnis iste natus error sit voluptatem accusantium doloremque laudantium, totam rem aperiam, eaque ipsa</p>
    <div class="f-social"><i></i><i></i><i></i></div>
  </div>
  <div>
    <h4>Contact Us</h4>
    <ul class="contact-list">
      <li><b>Address</b>48 Larkin Row, Suite C,<br>Millbrook, NC 27000</li>
      <li><b>Phone</b>+1 555 014 7590</li>
      <li><b>Email</b>info@redfernhollow.example</li>
    </ul>
  </div>
  <div>
    <h4>Feature Services</h4>
    <ul><li>Remodeling</li><li>New Home Construction</li><li>Additions</li></ul>
  </div>
  <div>
    <h4>Project Gallery</h4>
    <div class="thumbs" role="img" aria-label="Small photographs of completed projects"><i></i><i></i><i></i><i></i><i></i><i></i></div>
  </div>
</footer>

<div class="abs copyright">© 2018 REDFERN HOLLOW BUILDING COMPANY. ALL RIGHTS RESERVED.</div>

</body>
</html>
```